Gaphic explaining connectivity of research areas that use DNA analysis

We are a university research group in Perth Western Australia focused on ecology and environment fields. Our work can be explained by three broad areas where its applied - what used to be present ('ancient DNA analysis'), what is present now ('environmental DNA analysis') and what happened in terms of DNA based changes in between ('genomic changes'). To help simply convey this to other researchers and importantly non-science-savvy people we wanted an a eye catching rework of the attached for our website, future presentations, brochures etc. We didn't want it too visually complicated, nor wordy so something akin to the attached with a better look will help . More background on each point can be read on the website under construction here - https://natsci.belvane.edu.au/plimb-lab/

Target Market(s)

other science researchers in ecology, environment, geology, forensics areas, although ultimately its meant to be a simple way to understand for all people

Font styles to use
Sans Serif

Requirements
Must have
• the three areas indicated
Should not have
• design does not need to follow the colour pallet of the university (ie poo brown and black)

```html
<!DOCTYPE html>
<html lang="en">
<head>
<meta charset="utf-8">
<title>DNA research areas – connectivity graphic</title>
<link rel="stylesheet" href="https://fonts.googleapis.com/css2?family=Source+Sans+3:wght@700&display=swap">
<style>
  :root {
    --navy: #0e3f86;
    --blue-light: #1f7cc2;
    --blue-deep: #0d4a8c;
    --gold: #fbbf14;
    --ink: #151515;
    --white: #ffffff;
  }
  html, body {
    margin: 0;
    width: 906px;
    height: 1200px;
    overflow: hidden;
    background: var(--white);
  }
  .artboard {
    display: block;
    width: 906px;
    height: 1200px;
    font-family: "Source Sans 3", "Myriad Pro", Arial, sans-serif;
    font-weight: 700;
  }
  .ring { fill: none; stroke: var(--gold); stroke-width: 2.2; }
  .connector { fill: none; stroke: var(--gold); stroke-width: 2.2; }
  .node-dot { fill: var(--gold); }
  .disc { fill: var(--disc); }
  .label-pill { fill: var(--gold); }
  .area-name { fill: var(--navy); font-size: 25px; text-anchor: middle; }
  .area-question { fill: var(--question); font-size: 18px; text-anchor: middle; }
  .tagline { font-size: 25.5px; text-anchor: middle; }

  .version-light { --disc: url(#discGradient); --question: var(--white); }
  .version-light .tagline { fill: var(--ink); }
  .version-dark { --disc: var(--white); --question: var(--navy); }
  .version-dark .tagline { fill: var(--white); }
</style>
</head>
<body>
<svg class="artboard" viewBox="0 0 1000 1294" preserveAspectRatio="xMidYMid meet" xmlns="http://www.w3.org/2000/svg">
  <defs>
    <linearGradient id="discGradient" x1="0" y1="0" x2="1" y2="1">
      <stop offset="0" stop-color="#2285c9"/>
      <stop offset="1" stop-color="#0c4288"/>
    </linearGradient>
    <linearGradient id="panelGradient" x1="0" y1="0" x2="1" y2="0">
      <stop offset="0" stop-color="#1b74ba"/>
      <stop offset="1" stop-color="#0c4787"/>
    </linearGradient>

    <g id="research-diagram">
      <!-- connectors -->
      <path class="connector" d="M397 254 H303 Q286 254 286 271 V298"/>
      <path class="connector" d="M582 254 H674 Q691 254 691 271 V298"/>
      <path class="connector" d="M488 352 V490"/>
      <path class="connector" d="M379 397 H448 Q466 397 466 415 V490"/>
      <path class="connector" d="M597 397 H530 Q512 397 512 415 V490"/>

      <!-- aDNA -->
      <g class="area area-ancient">
        <circle class="ring" cx="488" cy="258" r="92"/>
        <circle class="disc" cx="488" cy="258" r="80"/>
        <rect class="label-pill" x="420" y="218" width="134" height="35" rx="17.5"/>
        <text class="area-name" x="487" y="245">aDNA</text>
        <text class="area-question" x="488" y="291">What used to</text>
        <text class="area-question" x="488" y="308">be present?</text>
      </g>

      <!-- eDNA -->
      <g class="area area-environmental">
        <circle class="ring" cx="286" cy="390" r="93"/>
        <circle class="disc" cx="286" cy="390" r="80"/>
        <rect class="label-pill" x="218" y="353" width="135" height="35" rx="17.5"/>
        <text class="area-name" x="285" y="380">eDNA</text>
        <text class="area-question" x="286" y="424">What is</text>
        <text class="area-question" x="286" y="442">present?</text>
      </g>

      <!-- Genomics -->
      <g class="area area-genomic">
        <circle class="ring" cx="691" cy="390" r="93"/>
        <circle class="disc" cx="691" cy="390" r="80"/>
        <rect class="label-pill" x="620" y="356" width="142" height="34" rx="17"/>
        <text class="area-name" x="691" y="382">Genomics</text>
        <text class="area-question" x="691" y="419">What happened</text>
        <text class="area-question" x="691" y="437">along the</text>
        <text class="area-question" x="691" y="455">way?</text>
      </g>

      <!-- node dots -->
      <circle class="node-dot" cx="397" cy="254" r="3.6"/>
      <circle class="node-dot" cx="582" cy="254" r="3.6"/>
      <circle class="node-dot" cx="286" cy="298" r="3.6"/>
      <circle class="node-dot" cx="691" cy="298" r="3.6"/>
      <circle class="node-dot" cx="488" cy="352" r="3.6"/>
      <circle class="node-dot" cx="379" cy="397" r="3.6"/>
      <circle class="node-dot" cx="597" cy="397" r="3.6"/>
      <circle class="node-dot" cx="466" cy="490" r="3.6"/>
      <circle class="node-dot" cx="488" cy="490" r="3.6"/>
      <circle class="node-dot" cx="512" cy="490" r="3.6"/>
    </g>
  </defs>

  <!-- Light version -->
  <g class="version-light">
    <use href="#research-diagram"/>
    <text class="tagline" x="488" y="537">Insight on the formation,  distribution, and</text>
    <text class="tagline" x="488" y="563">resilience of Australian biodiversity</text>
  </g>

  <!-- Dark version -->
  <g class="version-dark">
    <rect class="panel" x="166" y="628" width="662" height="465" fill="url(#panelGradient)"/>
    <use href="#research-diagram" transform="translate(6 489)"/>
    <text class="tagline" x="495" y="1016">Insight on the formation,  distribution, and</text>
    <text class="tagline" x="495" y="1042">resilience of Australian biodiversity</text>
  </g>
</svg>
</body>
</html>
```